【 概要 】
宿泊施設のキャンセル客に対するキャンセル料の回収
【 依頼内容 】 ・サイズ:A4 片面 ・ページ数:1ページ ・素材の用意(画像・文章等):相談して決めたいです ・デザイン内容:添付の文章を使用して欲しいです 【 デザインイメージ 】 ・ターゲット層:宿泊施設経営者 ・雰囲気:法律事務所らしさを残しつつ高級過ぎない ・参考デザイン:弊所ホームページ https://sora-bengoshi-kobe.net/ 同業他社LP https://inn.kyakuyoyaku.site/ 【 契約金額(税抜) 】 7万円 ※契約金額(税込)からシステム利用料を差し引いた金額が、ワーカーさまの受取金額となります その他ご質問等ありましたら、気軽にお問い合わせください。 ご応募をお待ちしております! |
ご丁寧にご対応頂きありがとうございます。
とても納得のいく出来栄えになりました。
皆さまご提案頂きありがとうございました。また機会があれば依頼させて頂きますのでよろしくお願いいたします。

```html
<!DOCTYPE html>
<html lang="ja">
<head>
<meta charset="UTF-8">
<title>キャンセルリカバー | 神戸そら法律事務所</title>
<link href="https://fonts.googleapis.com/css2?family=Noto+Sans+JP:wght@400;500;700;900&family=Noto+Serif+JP:wght@600;700;900&display=swap" rel="stylesheet">
<style>
:root{
  --navy:#1c2c5b;
  --orange:#e88a3c;
  --orange-soft:#fbe9d8;
  --red:#d8302a;
  --sky:#e6eef8;
  --ink:#2a2a2a;
  --muted:#666;
  --white:#fff;
}
*{margin:0;padding:0;box-sizing:border-box}
html,body{width:848px;height:1200px;overflow:hidden;background:var(--white)}
body{font-family:"Noto Sans JP",sans-serif;color:var(--ink);position:relative}

.hero{position:absolute;left:0;top:0;width:848px;height:400px;background:linear-gradient(180deg,#f4f6fa 0%,#e3e8f1 100%);overflow:hidden}
.hero-photo{position:absolute;right:0;top:0;width:420px;height:400px;background:linear-gradient(120deg,rgba(244,246,250,0) 0%,#b9c4d6 35%,#6f7f9c 75%,#3d4a66 100%)}
.hero-tag{position:absolute;left:42px;top:26px;font-size:15px;font-weight:700;color:var(--navy);letter-spacing:.05em}
.hero-title{position:absolute;left:36px;top:56px;font-family:"Noto Serif JP",serif;font-weight:900;font-size:52px;color:var(--navy);letter-spacing:.04em;white-space:nowrap}
.hero-rule{position:absolute;left:42px;top:138px;width:360px;height:2px;background:linear-gradient(90deg,#c8a24a,#e8d49a)}
.hero-lead{position:absolute;left:42px;top:152px;width:370px;font-size:17px;font-weight:700;line-height:1.6;color:var(--navy)}
.badges{position:absolute;left:38px;top:240px;display:flex;gap:24px}
.badge{width:92px;text-align:center}
.badge-circle{width:86px;height:86px;border-radius:50%;background:var(--white);border:3px solid var(--navy);margin:0 auto;display:flex;align-items:center;justify-content:center}
.badge-label{margin-top:8px;font-size:13px;font-weight:700;color:var(--white);background:var(--navy);border-radius:12px;padding:2px 0}

.flow{position:absolute;left:0;top:400px;width:848px;height:372px;background:var(--sky)}
.flow-title{position:absolute;left:0;width:848px;top:20px;text-align:center;font-family:"Noto Serif JP",serif;font-weight:700;font-size:26px;color:var(--navy)}
.flow-title span{font-family:"Noto Sans JP",sans-serif;font-size:15px;font-weight:500;margin-left:8px;color:var(--muted)}
.flow-steps{position:absolute;left:22px;top:66px;display:flex;align-items:center}
.step{width:178px;height:290px;background:var(--white);border-radius:8px;overflow:hidden;box-shadow:0 2px 6px rgba(28,44,91,.12)}
.step-head{background:var(--orange);color:var(--white);text-align:center;font-weight:700;font-size:15px;padding:7px 0}
.step-body{padding:10px 12px 0;font-size:11.5px;line-height:1.6;height:104px;font-weight:500}
.step-art{margin:8px auto 0;width:140px;height:140px;border-radius:6px;background:linear-gradient(135deg,var(--orange-soft),#f3c79c)}
.step-arrow{width:22px;display:flex;justify-content:center}

.fees{position:absolute;left:40px;top:790px;width:768px;height:300px}
.fees-head{font-size:21px;font-weight:900;color:var(--navy)}
.fees-head em{font-style:normal;color:var(--red);font-size:25px;border-bottom:3px solid var(--red)}
.fees-note{margin-top:8px;font-size:12px;color:var(--muted)}
.fees-rate{margin-top:26px;font-size:20px;font-weight:900;color:var(--navy)}
.fees-rate strong{color:var(--red);font-size:34px}
.fees-example{margin-top:8px;font-size:13.5px;font-weight:500;width:560px}
.fees-result{display:inline-block;margin-top:6px;background:var(--red);color:var(--white);font-weight:700;font-size:15px;padding:4px 10px}
.fees-fine{margin-top:6px;font-size:12.5px}
.fees-art{position:absolute;right:6px;top:70px;width:150px;height:150px;border-radius:8px;background:linear-gradient(135deg,#e4eaf4,#b8c6de)}
.fees-caution{position:absolute;left:0;top:268px;font-size:10.5px;color:var(--red)}

.footer{position:absolute;left:0;bottom:0;width:848px;height:104px;background:var(--white);border-top:6px solid var(--navy);display:flex;align-items:center;padding:0 40px;justify-content:space-between}
.firm{display:flex;align-items:center;gap:12px}
.firm-mark{width:34px;height:34px;background:var(--navy)}
.firm-name{font-family:"Noto Serif JP",serif;font-weight:700;font-size:24px;color:var(--navy)}
.firm-addr{margin-top:4px;font-size:11px;color:var(--muted);line-height:1.5}
.tel{display:flex;align-items:center;gap:10px}
.tel-label{background:var(--navy);color:var(--white);font-weight:700;font-size:14px;padding:3px 8px}
.tel-number{font-size:32px;font-weight:900;color:var(--navy);letter-spacing:.02em}
.contact-info{font-size:11.5px;color:var(--muted);line-height:1.5}
</style>
</head>
<body>

<section class="hero">
  <div class="hero-photo" role="img" aria-label="Businessman in a suit looking over a city skyline"></div>
  <p class="hero-tag">宿泊施設経営者・オーナー様向け!</p>
  <h1 class="hero-title">キャンセルリカバー</h1>
  <div class="hero-rule"></div>
  <p class="hero-lead">着手金無料・完全成功報酬でキャンセル料の請求を代理するサービスです。</p>
  <div class="badges">
    <div class="badge">
      <div class="badge-circle"><svg width="40" height="40" viewBox="0 0 40 40"><circle cx="20" cy="20" r="14" fill="none" stroke="#1c2c5b" stroke-width="3"/><text x="20" y="26" text-anchor="middle" font-size="16" font-weight="700" fill="#1c2c5b">¥</text></svg></div>
      <div class="badge-label">着手金無料</div>
    </div>
    <div class="badge">
      <div class="badge-circle"><svg width="40" height="40" viewBox="0 0 40 40"><path d="M9 21l7 7 15-16" fill="none" stroke="#1c2c5b" stroke-width="4" stroke-linecap="round" stroke-linejoin="round"/></svg></div>
      <div class="badge-label">完全成功報酬</div>
    </div>
    <div class="badge">
      <div class="badge-circle"><svg width="40" height="40" viewBox="0 0 40 40"><path d="M20 6v28M10 34h20M6 12h28M6 12l-4 10h8zM34 12l-4 10h8z" fill="none" stroke="#1c2c5b" stroke-width="2.5" stroke-linejoin="round"/></svg></div>
      <div class="badge-label">弁護士対応</div>
    </div>
  </div>
</section>

<section class="flow">
  <h2 class="flow-title">ご依頼の流れ<span>Flow</span></h2>
  <div class="flow-steps">
    <div class="step">
      <div class="step-head">キャンセル発生</div>
      <p class="step-body">・何度か電話したが対応してもらえない<br>・回収業務がわずらわしい<br>・一部の回収に留まっている</p>
      <div class="step-art" role="img" aria-label="Illustration of a phone call about a cancellation"></div>
    </div>
    <div class="step-arrow"><svg width="14" height="22" viewBox="0 0 14 22"><path d="M2 2l10 9-10 9z" fill="#e88a3c"/></svg></div>
    <div class="step">
      <div class="step-head">請求依頼</div>
      <p class="step-body">宿泊情報を共有するだけなので簡単</p>
      <div class="step-art" role="img" aria-label="Illustration of documents and scales of justice"></div>
    </div>
    <div class="step-arrow"><svg width="14" height="22" viewBox="0 0 14 22"><path d="M2 2l10 9-10 9z" fill="#e88a3c"/></svg></div>
    <div class="step">
      <div class="step-head">キャンセル料の回収</div>
      <p class="step-body">随時連絡<br>スピーディーに問題の解決しサポートをさせていただきます。</p>
      <div class="step-art" role="img" aria-label="Illustration of invoices and coins being collected"></div>
    </div>
    <div class="step-arrow"><svg width="14" height="22" viewBox="0 0 14 22"><path d="M2 2l10 9-10 9z" fill="#e88a3c"/></svg></div>
    <div class="step">
      <div class="step-head">お振込み</div>
      <p class="step-body">弁護士費用を差し引いた回収金を回収した月の翌月末までにお振込みいたします。</p>
      <div class="step-art" role="img" aria-label="Illustration of a bank transfer"></div>
    </div>
  </div>
</section>

<section class="fees">
  <p class="fees-head">ご依頼時に<em>弁護士費用は発生しない</em>のでお手軽・安心</p>
  <p class="fees-note">※キャンセル料回収後、そこから弁護士費用を差し引かせて頂くため、費用倒れになることはありません。</p>
  <p class="fees-rate">弁護士費用:回収金額の<strong>33</strong>%(税込)</p>
  <p class="fees-example">例)2泊2食付き2名宿泊費計55,000円を当日キャンセルされた場合</p>
  <p class="fees-result">弁護士費用18,150円を差し引いた36,850円が振込されます</p>
  <p class="fees-fine">(振込手数料はご依頼者様負担となります。)</p>
  <div class="fees-art" role="img" aria-label="Illustration of a lawyer presenting savings"></div>
  <p class="fees-caution">※当サービスはキャンセル料の回収を保証するものではありません。訴訟等を提起される場合、別途弁護士費用についてご相談させて頂きます。</p>
</section>

<footer class="footer">
  <div>
    <div class="firm">
      <div class="firm-mark"></div>
      <div class="firm-name">神戸そら法律事務所</div>
    </div>
    <p class="firm-addr">〒650-0021<br>兵庫県神戸市中央区三宮町9-14 そらビル 5階</p>
  </div>
  <div class="contact">
    <div class="tel">
      <span class="tel-label">TEL</span>
      <svg width="24" height="24" viewBox="0 0 24 24"><path d="M6 3l4 4-2 3c1 2 3 4 5 5l3-2 4 4-3 3C10 20 4 14 3 6z" fill="#1c2c5b"/></svg>
      <span class="tel-number">078-555-0192</span>
    </div>
    <p class="contact-info">営業時間:平日 9:00〜18:00 土日祝休業<br>https://sora-bengoshi-kobe.net/</p>
  </div>
</footer>

</body>
</html>
```